Transfer Falcon - Cloud Based Data Migration Service for IT Professionals

We are looking for a smart clean website design for an informational site about our services and as a main portal into the service itself. We would like the design completed in WORDPRESS so that it will easily connect with the service.

Transfer Falcon is a cloud based migration service providing (to start with) a online migration tool that we migrate Quillnet Relay mailboxes (email) with all the settings, attachments from one system to another.
The service is aimed at IT professionals, IT companies and IT departments so our customers will be very technology based.

The Service -
IT companies currently migrate email; data and databases. using a very time intensive process which is both expensive and means their customer potentially losses access to its IT for a significant period of time. Additionally there are risks with regards to compatibility between systems and loss of data.
Potential benefits include;
• cost savings
• improved customer service, including reduced downtime
• improved resilience of the process
We are therefore developing cloud based migration software/website which will automate the process, mitigating these issues, as well as providing additional benefits such as the ability to sort and migrate only certain areas of data or certain emails, to check the integrity of the data/emails moved and to also repair corrupted data and emails.
The system will effectively duplicate the data and emails onto the new system over the weeks prior to the completion date. This will enable the IT Company to complete a final synchronisation and then immediately switch over to the new system with no interruption to the end users.
There is also an added benefit that the end users can test the system (with their own data and emails) prior to the switch over date to ensure everything is in place and databases work correctly.
The system will be completely cloud based and therefore easy for the IT Companies to access. They will be able to purchase the use of the system using CoinDrop or credit card and will only need to purchase what they need, this will allow even small local IT companies the facilities which previously would have been cost prohibitive to them.

Some of the sites we like for reference are -
Lanterbox, brightkits, the sky shifter.

We already have a logo design see attached and the website will need to work with this design.
Please message me if you have any questions
We do have the logo in other file formats if required.
Many Thanks

Target Market(s)

IT Sector

Industry/Entity Type

It Service

Number of Pages Required

5+ page

Requirements
Must have
• Front Page
• About Us
• Contact Info
• Blog
• Benefits
• More Information
• Must be Mobile Phone Compatible/friendly
• Log in (button) and support button on all pages (possibley top right)

```html
<!DOCTYPE html>
<html lang="en">
<head>
<meta charset="utf-8">
<title>Transfer Falcon</title>
<link rel="stylesheet" href="https://fonts.googleapis.com/css2?family=Questrial&family=Montserrat:wght@500;600;700&family=Lora:ital@1&display=swap">
<style>
:root{
  --blue:#00a5dc;
  --blue-deep:#0a8fc4;
  --ink:#222;
  --muted:#8a8a8a;
  --white:#fff;
  --hero-dark:#2f3a45;
  --hero-mid:#7d8893;
  --line:#e3e3e3;
}
*{margin:0;padding:0;box-sizing:border-box}
html,body{width:686px;height:1200px;overflow:hidden;background:var(--white)}
body{position:relative;font-family:"Questrial",sans-serif;color:var(--ink)}
.abs{position:absolute}

/* hero */
.hero{left:0;top:0;width:686px;height:398px;background:linear-gradient(180deg,var(--hero-mid) 0%,#5c6773 45%,var(--hero-dark) 100%)}
.hero-visual{left:210px;top:110px;width:440px;height:260px;background:radial-gradient(ellipse at 60% 50%,#1d2228 0%,rgba(29,34,40,.6) 55%,rgba(29,34,40,0) 75%)}
.nav{top:27px;left:0;width:686px;height:14px;font-size:7.5px;color:var(--white);letter-spacing:.3px}
.nav a{position:absolute;color:var(--white);text-decoration:none;transform:translateX(-50%);white-space:nowrap}
.nav a.active{font-family:"Montserrat",sans-serif;font-weight:700}
.nav .sep{position:absolute;top:0;width:1px;height:8px;background:var(--white)}
.nav .marker{position:absolute;left:62px;top:16px;width:0;height:0;border-left:4px solid transparent;border-right:4px solid transparent;border-top:4px solid var(--blue)}
.brand{left:343px;top:18px;transform:translateX(-50%);display:flex;align-items:center;gap:4px;font-family:"Montserrat",sans-serif;font-weight:700;font-size:10px;line-height:11px;color:var(--blue);text-align:center}
.brand-dot{width:7px;height:7px;border-radius:50%;background:var(--blue);flex:none}
.login{right:45px;top:6px;font-size:5.5px;color:var(--white);display:flex;align-items:center;gap:2px}
.welcome{left:42px;top:124px;font-size:16px;color:var(--white);letter-spacing:.5px}
.hero-title{left:37px;top:140px;font-family:"Montserrat",sans-serif;font-weight:600;font-size:42px;line-height:39px;color:var(--blue);letter-spacing:-.5px}
.hero-text{left:40px;top:232px;width:248px;font-size:6px;line-height:7.6px;color:var(--white)}
.hero-text b{font-style:italic}
.btn-contact{left:37px;top:281px;width:108px;height:33px;border:2px solid var(--blue);color:var(--white);font-family:"Montserrat",sans-serif;font-weight:600;font-size:13px;display:flex;align-items:center;justify-content:center}
.dots{display:flex;gap:3px}
.dots span{width:9px;height:9px;border-radius:50%;background:#c8ccd0}
.dots span.on{background:var(--blue);border:1.5px solid #c8ccd0}
.hero-dots{left:326px;top:386px}

/* migrate */
.section-title{width:686px;left:0;text-align:center;font-family:"Montserrat",sans-serif;font-weight:600;font-size:12.5px;letter-spacing:.2px}
.migrate-title{top:411px}
.service{top:440px;width:120px;text-align:center}
.service .ring{width:74px;height:74px;margin:0 auto;border-radius:50%;border:2px solid var(--blue);display:flex;align-items:center;justify-content:center;background:var(--white)}
.service .ring.filled{background:var(--blue)}
.service h3{margin-top:7px;font-family:"Montserrat",sans-serif;font-weight:600;font-size:7px;white-space:nowrap}
.service p{margin:2px auto 0;width:74px;font-size:6px;line-height:7.2px;color:var(--muted);text-align:justify;text-align-last:center}
.divider{top:456px;width:1px;height:50px;background:var(--line)}

/* benefits */
.benefit-bar{left:38px;top:613px;width:5px;height:72px;background:var(--blue)}
.benefit-title{left:48px;top:609px;font-family:"Montserrat",sans-serif;font-weight:700;font-size:18px;line-height:27px;letter-spacing:-.2px;color:var(--ink);white-space:nowrap;z-index:2}
.benefit-text{left:40px;top:699px;width:210px;font-size:6px;line-height:7.7px;text-align:justify;color:#333}
.benefit-visual{left:265px;top:598px;width:383px;height:186px;background:linear-gradient(180deg,#ffffff 0%,#f4f4f4 40%,#3a3d44 100%)}

/* testimonial */
.testimonial{left:0;top:784px;width:686px;height:257px;background:var(--blue)}
.testimonial-title{top:799px;color:var(--white)}
.avatar{left:292px;top:833px;width:103px;height:103px;border-radius:50%;border:3px solid var(--white);background:linear-gradient(160deg,#f2c9a8,#5a4a42)}
.quote{font-family:"Lora",serif;font-size:58px;color:var(--white);line-height:1}
.quote-open{left:204px;top:927px}
.quote-close{left:446px;top:964px}
.testimonial-text{left:243px;top:951px;width:200px;font-family:"Lora",serif;font-style:italic;font-size:6.1px;line-height:9.8px;color:var(--white);text-align:center}
.testi-dots{left:326px;top:1027px}
.testi-dots span{background:var(--white);border:none}
.testi-dots span.on{background:var(--blue);border:1.5px solid var(--white)}

/* newsletter */
.news-title{top:1051px;color:var(--blue);font-size:12.5px}
.news-sub{left:0;top:1068px;width:686px;text-align:center;font-size:13px;color:#444}
.news-input{left:260px;top:1097px;width:113px;height:20px;background:var(--blue);color:var(--white);font-size:6.5px;padding:6px 8px}
.news-btn{left:377px;top:1097px;width:49px;height:20px;background:var(--blue);color:var(--white);font-size:6.5px;display:flex;align-items:center;justify-content:center;border:1px solid var(--blue-deep)}
.social{top:1136px;width:18px;height:18px;border-radius:50%;border:1px solid #bbb}
.social.active{background:var(--blue);border-color:var(--blue)}

/* footer */
.footer{left:0;top:1161px;width:686px;height:39px;background:var(--blue);color:var(--white)}
.copyright{left:39px;top:16px;font-size:6.2px}
.footer-links{left:239px;top:16px;font-family:"Montserrat",sans-serif;font-weight:500;font-size:5.8px;word-spacing:1px;white-space:nowrap}
.to-top{left:619px;top:15px}
</style>
</head>
<body>

<div class="abs hero"></div>
<div class="abs hero-visual" role="img" aria-label="Laptop floating on calm sea with a goldfish leaping from its screen"></div>

<nav class="abs nav">
  <a class="active" style="left:66px">HOME</a>
  <span class="sep" style="left:116px"></span>
  <a style="left:173px">ABOUT US</a>
  <span class="sep" style="left:230px"></span>
  <a style="left:281px">BLOGS</a>
  <a style="left:407px">SERVICES</a>
  <span class="sep" style="left:461px"></span>
  <a style="left:522px">CONTACT US</a>
  <span class="sep" style="left:583px"></span>
  <a style="left:630px">TEAM</a>
  <span class="marker"></span>
</nav>
<div class="abs brand"><span class="brand-dot"></span><span>Transfer<br>Falcon</span></div>
<div class="abs login">Log in
  <svg width="8" height="7" viewBox="0 0 8 7"><path d="M3 1H7V6H3" fill="none" stroke="#fff" stroke-width=".8"/><path d="M0 3.5H5M3.5 2L5 3.5 3.5 5" fill="none" stroke="#fff" stroke-width=".8"/></svg>
</div>

<div class="abs welcome">WELCOME</div>
<h1 class="abs hero-title">TRANSFER<br>FALCON</h1>
<p class="abs hero-text">Lorem Ipsum is simply dummy text of the printing and typesetting industry. Lorem Ipsum has been the industry's standard dummy text ever since the 1500s,Lorem Ipsum is simply dummy text of the printing and typesetting industry. <b>Read More</b></p>
<div class="abs btn-contact">Contact Now</div>
<div class="abs dots hero-dots"><span class="on"></span><span></span><span></span></div>

<h2 class="abs section-title migrate-title">WHAT WE MIGRATE</h2>

<div class="abs service" style="left:16px">
  <div class="ring filled">
    <svg width="40" height="34" viewBox="0 0 40 34"><rect x="6" y="4" width="20" height="14" fill="none" stroke="#fff" stroke-width="2.5"/><path d="M6 4L16 12 26 4" fill="none" stroke="#fff" stroke-width="2.5"/><path d="M2 14V28H22" fill="none" stroke="#fff" stroke-width="2.5"/><circle cx="28" cy="24" r="7" fill="none" stroke="#fff" stroke-width="2.5"/><path d="M24 24H32" stroke="#fff" stroke-width="2.5"/></svg>
  </div>
  <h3>Mailbox Migration</h3>
  <p>Lorem Ipsum is simply dummy text of the printing</p>
</div>
<div class="abs divider" style="left:141px"></div>
<div class="abs service" style="left:146px">
  <div class="ring">
    <svg width="26" height="30" viewBox="0 0 26 30"><rect x="7" y="1" width="16" height="22" fill="#6f6f6f"/><rect x="3" y="5" width="16" height="23" fill="#6f6f6f" stroke="#fff" stroke-width="1.2"/><path d="M6 12H16M6 16H16M6 20H16" stroke="#fff" stroke-width="1.3"/></svg>
  </div>
  <h3>File Migration</h3>
  <p>Lorem Ipsum is simply dummy text of the printing</p>
</div>
<div class="abs divider" style="left:271px"></div>
<div class="abs service" style="left:276px">
  <div class="ring">
    <svg width="30" height="28" viewBox="0 0 30 28"><path d="M2 6H11L13 9H27V25H2Z" fill="#6f6f6f"/><rect x="9" y="2" width="14" height="16" fill="#fff" stroke="#6f6f6f"/><path d="M2 25L6 13H29L26 25Z" fill="#8a8a8a"/></svg>
  </div>
  <h3>Public Folder Migration</h3>
  <p>Lorem Ipsum is simply dummy text of the printing</p>
</div>
<div class="abs divider" style="left:401px"></div>
<div class="abs service" style="left:406px">
  <div class="ring">
    <svg width="30" height="28" viewBox="0 0 30 28"><rect x="10" y="2" width="18" height="14" fill="none" stroke="#6f6f6f" stroke-width="2"/><rect x="6" y="6" width="18" height="14" fill="#fff" stroke="#6f6f6f" stroke-width="2"/><path d="M2 11H9L11 13H20V26H2Z" fill="#6f6f6f"/><path d="M11 16V23M7.5 19.5H14.5" stroke="#fff" stroke-width="2"/></svg>
  </div>
  <h3>Mailbox Archive Migration</h3>
  <p>Lorem Ipsum is simply dummy text of the printing</p>
</div>
<div class="abs divider" style="left:531px"></div>
<div class="abs service" style="left:536px">
  <div class="ring">
    <svg width="30" height="24" viewBox="0 0 30 24"><g fill="none" stroke="#6f6f6f" stroke-width="2"><rect x="2" y="2" width="7" height="20"/><rect x="11.5" y="2" width="7" height="20"/><rect x="21" y="2" width="7" height="20"/></g><path d="M3.5 8H7.5M13 8H17M22.5 8H26.5" stroke="#6f6f6f" stroke-width="2"/></svg>
  </div>
  <h3>Enterprise Archive Migration</h3>
  <p>Lorem Ipsum is simply dummy text of the printing</p>
</div>

<div class="abs benefit-visual" role="img" aria-label="Three business people in suits holding fishbowls with goldfish jumping between them"></div>
<div class="abs benefit-bar"></div>
<h2 class="abs benefit-title">WHAT ARE THE<br>BENEFITS TO WORK<br>WITH US</h2>
<p class="abs benefit-text">Lorem Ipsum is simply dummy text of the printing and typesetting industry. Lorem Ipsum has been the industry's standard dummy text ever since the 1500s, when an unknown printer took a galley of type and scrambled it to make a type specimen book. It has survived not only five centuries, but also the leap into electronic typesetting, remaining essentially unchanged. It was popularised in the 1960s with the release of Typeleaf sheets containing Lorem Ipsum passages, and more recently with desktop publishing software like Pagecraft Studio including versions of Lorem Ipsum.</p>

<div class="abs testimonial"></div>
<h2 class="abs section-title testimonial-title">WHAT OTHERS SAY ABOUT US</h2>
<div class="abs avatar" role="img" aria-label="Portrait of a smiling satisfied customer"></div>
<div class="abs quote quote-open">&ldquo;</div>
<p class="abs testimonial-text">Lorem Ipsum is simply dummy text of the printing and typesetting industry. Lorem Ipsum has been the industry's standard dummy text ever since the 1500s, when an unknown printer took a galley of with the release of Typeleaf sheets containing Lorem Ipsum passag</p>
<div class="abs quote quote-close">&rdquo;</div>
<div class="abs dots testi-dots"><span class="on"></span><span></span><span></span></div>

<h2 class="abs section-title news-title">TRANSFER FALCON</h2>
<p class="abs news-sub">Subscribe to our Newsletter for latest news.</p>
<div class="abs news-input">Email address</div>
<div class="abs news-btn">Subscribe</div>

<div class="abs social" style="left:287px"></div>
<div class="abs social active" style="left:318px"></div>
<div class="abs social" style="left:349px"></div>
<div class="abs social" style="left:381px"></div>

<footer class="abs footer">
  <div class="abs copyright">Copyright 2016 Transfer Falcon</div>
  <div class="abs footer-links">HOME &nbsp;| &nbsp;ABOUT US &nbsp;| &nbsp;BLOGS &nbsp;| &nbsp;CONTACT US &nbsp;| &nbsp;SERVICES &nbsp;| &nbsp;TEAM</div>
  <svg class="abs to-top" width="9" height="6" viewBox="0 0 9 6"><path d="M1 5L4.5 1.5 8 5" fill="none" stroke="#fff" stroke-width="1.6"/></svg>
</footer>

</body>
</html>
```